Create 8 Featured Images for 8 Blog articles

We're looking for a an individual with a background in graphic design to creatively process images for a popular product blog. This project will be to create 8 Featured images for our Blog which can be seen here http://www.brakwelsupply.com/blog the featured image is the large image which can be seen through the link above. If all goes well with this first project then there will be many additional graphic design projects available for our blog.

1. My Pool Pump is Running Too Hot - Article can be seen here http://www.brakwelsupply.com/blog/why-is-my-motor-running-hot/ We would like an Image of 750 x 250 of a pool pump in the desert or under the sun. Something obvious. We are trying to convey the message of an extremely hot pump. For the Desert or Sun use an image of your liking and for the pool pump use the attached image labeled “Hot Pump.jpg” (remove text from this image) Add text to image which says "Pool Pump Running Hot?"

2. Leaking pool pump - Article can be seen here http://www.brakwelsupply.com/blog/leaking-pool-pump/ Image to be created would be a leaking pool pump which is gushing out water similar to what is shown here http://www.tandrick-aqua-care.com/pool-closings.html but we would like for this to look much cleaner. The background of the image should be similar in color and style of the image backgrounds which can be seen here http://www.brakwelsupply.com/blog/ For the pool pump use the attached image labeled “Leaking Pump.jpg” and then photoshop gushing water out of the pump. Add text to image which says "Leaking Pool Pump?"

3. Can I go with a higher Horse Power Pump - article can be seen here http://www.brakwelsupply.com/blog/can-go-higher-horsepower-pump/ Image of a large pool pump vs. a small pump - You can exagerate the size of the large pump and exagerate the size of the small pump. The idea is to show a really big looking pump vs. a small looking pump. Attached image for the large pump is labeled “Large Pump.jpg” and Attached image of small pump is labeled “Small Pump.jpg” Add text to image which says "Large HP Vs. Small HP"

4. Pool Pump Trips Breaker - Article can be seen here http://www.brakwelsupply.com/blog/pool-pump-trips-breaker-gfci/ This will be a simple Image of a pool pump and a breaker spaced out evenly. Use attached image of of pool pump labeled “Pool Pump Breaker.jpg” and for the breaker use the attached image labeled “Breaker.jpg” Add text to image which says "Pool Pump Tripping Breaker?"

5. Why is my spa dirty? - Article can be seen here http://www.brakwelsupply.com/blog/spa-dirty/ use attached image labeled spa set on white backgroud with Text which says "Dirty Spa?"

6. Think You’re Cut out to Replace Your Pool Pump Motor? Take This Quiz - Article here -
http://www.brakwelsupply.com/blog/think-youre-cut-replace-pool-pump-motor-take-quiz/ Image integrating Quiz.jpg image and motor.jpg image with Text labeled "Take the Pool Motor Replacement Quiz"

7. Can I repair my pool Equipment - article here http://www.brakwelsupply.com/blog/can-i-repair-my-pool-equipment/ - A guy holding tools with a question mark thought bubble.

8. How Long should I run my pool pump article here -http://www.brakwelsupply.com/blog/how-long-should-i-run-my-pool-pump/ - image of a pool pump along with a man looking at his watch.

```html
<!DOCTYPE html>
<html lang="en">
<head>
<meta charset="utf-8">
<title>Brakwelsupply Blog</title>
<link href="https://fonts.googleapis.com/css2?family=Open+Sans:wght@400;600;700&family=Arimo:wght@700&family=Oswald:wght@500&display=swap" rel="stylesheet">
<style>
  :root{
    --header-blue:#1f6798;
    --page-bg:#f1f1f1;
    --card-bg:#ffffff;
    --card-border:#dcdcdc;
    --accent-orange:#e2632b;
    --button-blue:#3b8cbe;
    --text-body:#555555;
    --text-muted:#9a9a9a;
    --heading-grey:#555555;
    --rule:#e4e4e4;
    --sky-top:#3d8fd6;
    --sky-mid:#a9d3f2;
    --sand-light:#e9c477;
    --sand-deep:#c98d2e;
    --pump-dark:#1e1e1e;
    --pump-mid:#3a3a3a;
  }
  *{box-sizing:border-box;margin:0;padding:0}
  html,body{width:1200px;height:706px;overflow:hidden}
  body{background:var(--page-bg);font-family:"Open Sans",Arial,sans-serif;position:relative;color:var(--text-body)}
  .site-header{position:absolute;left:0;top:0;width:1200px;height:76px;background:var(--header-blue)}
  .brand{position:absolute;left:30px;top:6px;display:flex;align-items:center;gap:10px}
  .brand-mark{width:46px;height:46px;border-radius:50%;background:#3f9fe0}
  .brand-name{font-family:"Open Sans",Arial,sans-serif;font-weight:700;font-size:22px;color:#fff;letter-spacing:.5px;margin-top:22px}
  .main-nav{position:absolute;right:62px;top:29px;display:flex;gap:34px}
  .main-nav a{color:#fff;text-decoration:none;font-size:14px;letter-spacing:.2px}
  .post-card{position:absolute;left:28px;top:121px;width:750px;height:600px;background:var(--card-bg);border:1px solid var(--card-border)}
  .featured-image{position:absolute;left:4px;top:4px;width:740px;height:240px;overflow:hidden;
    background:linear-gradient(180deg,var(--sky-top) 0%,var(--sky-mid) 52%,var(--sand-light) 66%,var(--sand-deep) 100%)}
  .featured-product{position:absolute;left:22px;top:24px;width:240px;height:190px;border-radius:18px 30px 14px 40px;
    background:linear-gradient(135deg,var(--pump-mid),var(--pump-dark))}
  .featured-title{position:absolute;left:285px;top:78px;font-family:"Oswald","Bebas Neue",sans-serif;font-weight:500;font-size:42px;line-height:1;color:#fff;letter-spacing:-.3px;white-space:nowrap;text-shadow:2px 3px 4px rgba(0,0,0,.45)}
  .post-body{position:absolute;left:0;top:249px;width:748px;border-top:1px solid var(--card-border)}
  .post-title{position:absolute;left:50px;top:42px;font-family:"Arimo",Arial,sans-serif;font-weight:700;font-size:28px;color:var(--accent-orange);white-space:nowrap}
  .post-meta{position:absolute;left:50px;top:110px;display:flex;gap:14px;font-size:13px;color:var(--text-body);white-space:nowrap}
  .post-meta span{display:flex;align-items:center;gap:6px}
  .post-excerpt{position:absolute;left:50px;top:159px;width:650px;font-size:14px;line-height:23px}
  .read-more{position:absolute;left:602px;top:271px;width:96px;height:41px;border-radius:3px;background:var(--button-blue);color:#fff;font-size:12px;display:flex;align-items:center;justify-content:center;border:1px solid #2f77a4}
  .sidebar{position:absolute;left:808px;top:121px;width:360px;height:600px;background:var(--card-bg);border:1px solid var(--card-border);border-radius:3px}
  .search{position:absolute;left:30px;top:30px;width:299px;height:34px;display:flex}
  .search-field{flex:1;border:1px solid #cfcfcf;font-size:14px;color:#888;padding:7px 4px}
  .search-button{width:40px;background:var(--button-blue);border-radius:0 3px 3px 0;display:flex;align-items:center;justify-content:center}
  .widget-title{position:absolute;left:30px;font-size:13px;font-weight:700;color:var(--heading-grey);letter-spacing:.3px;text-transform:uppercase}
  .recent-posts{position:absolute;left:30px;top:144px;width:298px;list-style:none}
  .recent-posts li{height:57px;padding-top:9px;overflow:hidden;border-bottom:1px solid var(--rule);font-size:14px;line-height:18px;color:var(--text-muted)}
  .recent-posts time{color:var(--accent-orange)}
  .archives{position:absolute;left:30px;top:518px;width:298px;list-style:none}
  .archives li{height:38px;border-bottom:1px solid var(--rule);font-size:14px;color:var(--text-muted);display:flex;align-items:center;gap:8px}
</style>
</head>
<body>
  <header class="site-header">
    <div class="brand"><span class="brand-mark"></span><span class="brand-name">BRAKWELSUPPLY.COM</span></div>
    <nav class="main-nav"><a href="#">SHOP BRAKWELSUPPLY</a><a href="#">MY ACCOUNT</a><a href="#">VIEW CART</a></nav>
  </header>

  <article class="post-card">
    <div class="featured-image" role="img" aria-label="Sunlit desert with dunes under a bright blue sky">
      <div class="featured-product" role="img" aria-label="Black pool pump with motor standing on the sand"></div>
      <div class="featured-title">POOL PUMP RUNNING HOT?</div>
    </div>
    <div class="post-body">
      <h1 class="post-title">Getting DE Powder Back in Your Pool</h1>
      <div class="post-meta">
        <span><svg width="13" height="13" viewBox="0 0 13 13"><rect x="1" y="2" width="11" height="10" fill="none" stroke="#e2632b" stroke-width="1.4"/><rect x="1" y="2" width="11" height="3" fill="#e2632b"/></svg>December 17, 2014</span>
        <span><svg width="11" height="13" viewBox="0 0 11 13"><circle cx="5.5" cy="3.5" r="3" fill="#e2632b"/><path d="M0 13c0-4 2.5-6 5.5-6s5.5 2 5.5 6z" fill="#e2632b"/></svg>Dana Whitcomb</span>
        <span><svg width="14" height="12" viewBox="0 0 14 12"><path d="M7 1C3.5 1 1 3 1 5.3c0 1.3.8 2.4 2 3.2L2.5 11l3-1.8c.5.1 1 .1 1.5.1 3.5 0 6-2 6-4S10.5 1 7 1z" fill="none" stroke="#e2632b" stroke-width="1.3"/></svg>2 Comments</span>
      </div>
      <p class="post-excerpt">Few things are more frustrating than to see the very stuff that is supposed to be filtering your pool water leaking into the pool.&nbsp; The common culprit involved in DE powder going back into your pool is torn grids but there are a number of other causes as well.&nbsp; Here are a few things to check to help you troubleshoot this annoying problem.</p>
      <a class="read-more">READ MORE</a>
    </div>
  </article>

  <aside class="sidebar">
    <div class="search">
      <div class="search-field">Search...</div>
      <div class="search-button"><svg width="15" height="15" viewBox="0 0 15 15"><circle cx="6" cy="6" r="4.5" fill="none" stroke="#fff" stroke-width="2"/><path d="M9.5 9.5L14 14" stroke="#fff" stroke-width="2.4" stroke-linecap="round"/></svg></div>
    </div>
    <h2 class="widget-title" style="top:113px">Our Recent Posts &amp; Articles</h2>
    <ul class="recent-posts">
      <li>Getting DE Powder Back in Your Pool<br><time>December 17, 2014</time></li>
      <li>Are Generic Parts Better Than OEM?<br><time>December 12, 2014</time></li>
      <li>5 Biggest Problems with Pool Filters<br><time>December 12, 2014</time></li>
      <li>Pool Pump Trips Breaker / GFCI <time>October 29, 2014</time></li>
      <li>Can I Go With A Higher Horsepower Pump?<br><time>October 23, 2014</time></li>
    </ul>
    <h2 class="widget-title" style="top:488px">Archives</h2>
    <ul class="archives">
      <li><svg width="13" height="13" viewBox="0 0 13 13"><rect x="1" y="2" width="11" height="10" fill="none" stroke="#e2632b" stroke-width="1.4"/><rect x="1" y="2" width="11" height="3" fill="#e2632b"/></svg>December 2014</li>
      <li><svg width="13" height="13" viewBox="0 0 13 13"><rect x="1" y="2" width="11" height="10" fill="none" stroke="#e2632b" stroke-width="1.4"/><rect x="1" y="2" width="11" height="3" fill="#e2632b"/></svg>October 2014</li>
    </ul>
  </aside>
</body>
</html>
```